Renata Quisby

Luxury And Style -

Black - White & Gold

Target Market(s)

Fashion

Industry/Entity Type

Fashion

Requirements
Must have
• High-End
Nice to have
• We will Print on Silk Paper

```html
<!DOCTYPE html>
<html lang="en">
<head>
<meta charset="utf-8">
<title>Renata Quisby – Letterhead</title>
<link href="https://fonts.googleapis.com/css2?family=Arimo:wght@400&family=Tinos:wght@400&display=swap" rel="stylesheet">
<style>
  :root{
    --backdrop:#e0e0e0;
    --paper:#ffffff;
    --ink:#000000;
    --gold:#c6a060;
    --gold-light:#e6c58f;
    --text:#111111;
  }
  *{margin:0;padding:0;box-sizing:border-box}
  html,body{width:1200px;height:1200px;overflow:hidden;background:var(--backdrop)}
  .letterhead{
    position:absolute;left:216px;top:75px;width:770px;height:1084px;
    background:var(--paper);box-shadow:4px 6px 14px rgba(0,0,0,.18);overflow:hidden;
  }
  .header-band{position:absolute;left:2px;top:1px;width:768px;height:97px;background:var(--ink)}
  .header-rule{position:absolute;left:2px;top:103px;width:768px;height:3px;
    background:linear-gradient(90deg,var(--gold),var(--gold-light))}
  .brand-seal{
    position:absolute;left:303px;top:3px;width:176px;height:176px;border-radius:50%;
    background:var(--ink);border:6px solid var(--gold);
    display:flex;align-items:center;justify-content:center;
  }
  .brand-name{
    font-family:'Arimo',sans-serif;font-weight:400;font-size:15px;letter-spacing:2px;
    color:var(--gold);text-transform:uppercase;white-space:nowrap;
  }
  .letter-body{
    position:absolute;left:105px;top:332px;width:538px;
    font-family:'Arimo',sans-serif;font-size:15px;line-height:17.4px;color:var(--text);
    text-align:justify;
  }
  .letter-body p{margin-bottom:35px}
  .letter-body p.short{margin-bottom:35px}
  .footer-wave{position:absolute;left:0;top:863px;width:770px;height:221px}
  .contact{position:absolute;font-family:'Tinos',serif;font-size:21px;color:#fff;white-space:nowrap;line-height:24px}
  .contact-icon{position:absolute;width:18px;height:18px}
  .contact-icon path,.contact-icon circle{fill:var(--gold)}
</style>
</head>
<body>
<main class="letterhead">
  <div class="header-band"></div>
  <div class="header-rule"></div>
  <div class="brand-seal"><span class="brand-name">Renata Quisby</span></div>

  <section class="letter-body">
    <p>Lorem ipsum dolor sit amet, consectetur adipiscing elit. Donec fringilla neque euismod volutpat cursus. Vestibulum ac pretium orci, consequat elementum velit. Etiam bibendum purus ac augue finibus volutpat. Vestibulum justo nisl</p>
    <p>Lorem ipsum dolor sit amet, consectetur adipiscing elit. Donec fringilla neque euismod volutpat cursus. Vestibulum ac pretium orci, consequat elementum velit. Etiam bibendum purus ac augue finibus volutpat. Vestibulum justo nisl, gravida aliquet sollicitudin ut, finibus vitae mi. Praesent aliquet scelerisque blandit. Sed id varius lacus, id tristique sem. Fusce et lobortis leo. Aliquam mollis pellentesque magna, condimentum ullamcorper ex ullamcorper non. Morbi ultricies nunc eu tellus dignissim, eget venenatis dolor ullamcorper. Etiam dolor eros, iaculis at ultricies nec, volutpat nec orci. Vivamus tincidunt rutrum sapien, ac porttitor mauris tristique nec.</p>
    <p>Lorem ipsum dolor sit amet, consectetur adipiscing elit. Donec fringilla neque euismod volutpat cursus. Vestibulum ac pretium orci, consequat elementum velit. Etiam bibendum purus ac augue finibus volutpat. Vestibulum justo nisl, gravida aliquet sollicitudin ut, finibus vitae mi. Praesent aliquet scelerisque blandit. Sed id varius lacus, id tristique sem. Fusce et lobortis leo. Aliquam mollis pellentesque magna, condimentum ullamcorper ex ullamcorper non. Morbi ultricies nunc eu tellus dignissim, eget venenatis dolor ullamcorper. Etiam dolor eros, iaculis at ultricies nec, volutpat nec orci. Vivamus tincidunt rutrum sapien, ac porttitor mauris tristique nec.</p>
    <p>Lorem ipsum dolor sit amet, consectetur adipiscing elit. Donec fringilla neque euismod volutpat cursus. Vestibulum ac pretium orci, consequat elementum velit. Etiam bibendum purus ac augue finibus volutpat. Vestibulum justo nisl</p>
  </section>

  <svg class="footer-wave" viewBox="0 0 770 221" aria-hidden="true">
    <path d="M2,62 Q385,180 762,50 L762,221 L2,221 Z" fill="var(--ink)"/>
    <path d="M2,40 Q380,160 741,22 Q380,187 2,52 Z" fill="var(--gold)"/>
  </svg>

  <svg class="contact-icon" style="left:164px;top:1019px" viewBox="0 0 24 24" aria-hidden="true">
    <path d="M6.6 10.8a15.1 15.1 0 0 0 6.6 6.6l2.2-2.2c.3-.3.7-.4 1-.2 1.1.4 2.3.6 3.6.6.6 0 1 .4 1 1V20c0 .6-.4 1-1 1A17 17 0 0 1 3 4c0-.6.4-1 1-1h3.5c.6 0 1 .4 1 1 0 1.3.2 2.5.6 3.6.1.3 0 .7-.2 1z"/>
  </svg>
  <div class="contact" style="left:194px;top:1003px">044-310 672 845</div>

  <svg class="contact-icon" style="left:164px;top:1049px" viewBox="0 0 24 24" aria-hidden="true">
    <path d="M2 5h20v14H2z M3.5 6.5v.4L12 13l8.5-6.1v-.4z" fill-rule="evenodd"/>
  </svg>
  <div class="contact" style="left:194px;top:1034px">hello@quisbyatelier.com</div>

  <svg class="contact-icon" style="left:436px;top:1012px" viewBox="0 0 24 24" aria-hidden="true">
    <path d="M12 2a10 10 0 1 0 0 20 10 10 0 0 0 0-20zm0 2a8 8 0 0 1 7.4 5H15l-2 2 1 3-2 3v3.9A8 8 0 0 1 5 8l3 2 1 3 2-1-1-4 2-2z"/>
  </svg>
  <div class="contact" style="left:465px;top:997px">www.quisbyatelier.com</div>

  <svg class="contact-icon" style="left:436px;top:1041px;height:22px" viewBox="0 0 24 28" aria-hidden="true">
    <path d="M12 0a9 9 0 0 0-9 9c0 7 9 19 9 19s9-12 9-19a9 9 0 0 0-9-9zm0 13a4 4 0 1 1 0-8 4 4 0 0 1 0 8z"/>
  </svg>
  <div class="contact" style="left:461px;top:1026px">87, Velmont Arcade<br>Sorrelhaven, 30718</div>
</main>
</body>
</html>
```